New Business Cards for Organic Meat Farm

We need a business card designed for Thornbury Farm, a meat farm in western MA. Our logo uses a hand-drawn woodcut (attached). Our color palette has been simply black and white (shown in notepad and picture of our food truck). While we are based out of western MA, we have ambitions to grow nationally, so our hope is for a classy and memorable card which will be printed on a premium quality stock from a printer like printkestrel.com.
Target Market(s)
consumers of quality meats, restauranteurs, partnering farms
Industry/Entity Type
Farming and prepared meat products
Contact Information for Business Card
Wendell Pruitt, President/Owner, wendell@thornburyfarm.com, mobile: 413-555-0172, phone: 413-555-0148, thornburyfarm.com, facebook: @thornburyfarm, instagram: @thornburyfarmma
Colors
Designer to choose colors to be used in the design.
Look and feel

```html
<!DOCTYPE html>
<html lang="en">
<head>
<meta charset="utf-8">
<title>Thornbury Farm – Business Card</title>
<link href="https://fonts.googleapis.com/css2?family=Montserrat:wght@400;500&display=swap" rel="stylesheet">
<style>
  :root {
    --ink: #161616;
    --paper: #ffffff;
    --silver-light: #e6e6e6;
    --silver-dark: #8a8a8a;
    --backdrop: #4a4a4a;
    --text-light: #f2f2f2;
  }
  html, body {
    margin: 0;
    width: 1200px;
    height: 1200px;
    overflow: hidden;
    background: var(--backdrop);
    font-family: "Montserrat", sans-serif;
  }
  .card {
    position: absolute;
    left: 250px;
    width: 700px;
    height: 400px;
    border-radius: 28px;
    overflow: hidden;
    box-shadow: 0 14px 30px rgba(0,0,0,0.45);
  }
  .card-front { top: 150px; background: var(--paper); }
  .card-back { top: 650px; background: var(--ink); }

  .front-panel { position: absolute; inset: 0; }

  .contact {
    position: absolute;
    left: 40px;
    top: 78px;
    color: var(--text-light);
  }
  .contact-name {
    margin: 0;
    font-size: 27px;
    font-weight: 500;
    letter-spacing: 0.3px;
    text-transform: uppercase;
    white-space: nowrap;
  }
  .contact-title {
    margin: 0 0 16px;
    font-size: 14px;
    font-weight: 400;
    letter-spacing: 0.5px;
    text-transform: uppercase;
  }
  .contact-list { list-style: none; margin: 0; padding: 0; }
  .contact-item {
    display: flex;
    align-items: center;
    gap: 10px;
    font-size: 16px;
    line-height: 25px;
    white-space: nowrap;
  }
  .contact-item svg { width: 18px; height: 18px; flex: none; }
  .social { margin-top: 12px; }
  .social .contact-item { font-size: 15px; line-height: 22px; gap: 6px; }
  .social-mark {
    width: 12px; height: 12px;
    border: 1.5px solid var(--text-light);
    border-radius: 2px;
    flex: none;
  }

  .brand {
    position: absolute;
    display: flex;
    flex-direction: column;
    align-items: center;
    gap: 18px;
  }
  .brand-dot {
    width: 64px; height: 64px;
    border-radius: 50%;
  }
  .brand-name {
    font-size: 30px;
    font-weight: 500;
    letter-spacing: 1px;
    white-space: nowrap;
  }
  .card-front .brand { left: 415px; width: 270px; top: 120px; }
  .card-front .brand-dot { background: var(--ink); }
  .card-front .brand-name { color: var(--ink); }
  .card-back .brand { left: 0; width: 700px; top: 125px; }
  .card-back .brand-dot { background: var(--text-light); }
  .card-back .brand-name { color: var(--text-light); font-size: 44px; }
</style>
</head>
<body>

<section class="card card-front">
  <svg class="front-panel" viewBox="0 0 700 400" preserveAspectRatio="none" aria-hidden="true">
    <defs>
      <linearGradient id="silver-swoosh" x1="0" y1="0" x2="0" y2="1">
        <stop offset="0" stop-color="var(--silver-light)"/>
        <stop offset="0.6" stop-color="var(--silver-dark)"/>
        <stop offset="1" stop-color="var(--silver-light)"/>
      </linearGradient>
    </defs>
    <path d="M0,0 H312 C382,110 422,250 397,400 H0 Z" fill="url(#silver-swoosh)"/>
    <path d="M0,0 H300 C370,110 410,250 385,400 H0 Z" fill="var(--ink)"/>
  </svg>

  <div class="contact">
    <h1 class="contact-name">Wendell Pruitt</h1>
    <p class="contact-title">President/Owner</p>
    <ul class="contact-list">
      <li class="contact-item">
        <svg viewBox="0 0 18 18"><rect x="5" y="1.5" width="8" height="15" rx="1.5" fill="none" stroke="currentColor" stroke-width="1.5"/><circle cx="9" cy="14" r="0.9" fill="currentColor"/></svg>
        413-555-0172
      </li>
      <li class="contact-item">
        <svg viewBox="0 0 18 18"><path d="M4 2 L7 2 L8 6 L6 7.5 C7 10 8.5 11.5 11 12.5 L12.5 10.5 L16 11.5 L16 14.5 C16 15.5 15 16 14 16 C8 15.5 2.5 10 2 4 C2 3 3 2 4 2 Z" fill="currentColor"/></svg>
        413-555-0148
      </li>
      <li class="contact-item">
        <svg viewBox="0 0 18 18"><rect x="1.5" y="4" width="15" height="10" fill="none" stroke="currentColor" stroke-width="1.5"/><path d="M1.5 4 L9 10 L16.5 4" fill="none" stroke="currentColor" stroke-width="1.5"/></svg>
        wendell@thornburyfarm.com
      </li>
      <li class="contact-item">
        <svg viewBox="0 0 18 18" fill="none" stroke="currentColor" stroke-width="1.3"><circle cx="9" cy="9" r="7.5"/><ellipse cx="9" cy="9" rx="3.2" ry="7.5"/><path d="M1.5 9 H16.5 M3 5 H15 M3 13 H15"/></svg>
        thornburyfarmma
      </li>
    </ul>
    <ul class="contact-list social">
      <li class="contact-item"><span class="social-mark"></span>@thornburyfarm</li>
      <li class="contact-item"><span class="social-mark"></span>@thornburyfarm</li>
    </ul>
  </div>

  <div class="brand">
    <div class="brand-dot" role="img" aria-label="Woodcut farmhouse illustration from the farm logo"></div>
    <div class="brand-name">Thornbury Farm</div>
  </div>
</section>

<section class="card card-back">
  <div class="brand">
    <div class="brand-dot" role="img" aria-label="Woodcut farmhouse illustration from the farm logo"></div>
    <div class="brand-name">Thornbury Farm</div>
  </div>
</section>

</body>
</html>
```